KelvrasMassage website required

We need a website for a mobile sports massage therapist in the United Kingdom. Specialising in pregnancy and postnatal massage, sports and remedial, deep tissue massage & Corprate Massage. Attached are some logos that we already have in various colours. The file named logo_white_background is what we normally use. Feel free to use the others at your discretion.

Requirements
Must have
• Service areas, Booking system.

```html
<!DOCTYPE html>
<html lang="en">
<head>
<meta charset="utf-8">
<title>Kelvra's Massage</title>
<link rel="stylesheet" href="https://fonts.googleapis.com/css2?family=Montserrat:wght@400;500;600;700&display=swap">
<style>
:root{
  --cyan:#00cfff;
  --green:#0ce07a;
  --teal:#14c9b0;
  --teal-dark:#23717f;
  --send-green:#138f7a;
  --brand-blue:#1bb8e8;
  --ink:#1a1a1a;
  --white:#ffffff;
  --photo-warm:#e9b78a;
  --photo-light:#f6e4cf;
}
*{box-sizing:border-box;margin:0;padding:0}
html,body{width:1200px;height:2514px;overflow:hidden}
body{position:relative;background:var(--white);font-family:'Montserrat',sans-serif;color:var(--ink)}
.abs{position:absolute}

/* header + hero */
.hero-photo{left:0;top:120px;width:1200px;height:497px;
  background:linear-gradient(100deg,var(--photo-light) 0%,var(--photo-warm) 45%,#d99a6a 70%,var(--photo-light) 100%)}
.header-band{left:0;top:0;width:1200px;height:240px}
.brand{left:112px;top:40px;width:150px;color:var(--white);font-weight:600;text-align:center}
.brand-name{font-size:34px;line-height:40px}
.brand-sub{font-size:15px;letter-spacing:8px;line-height:22px;margin-top:4px}
.nav{top:56px;font-size:19px;font-weight:500;color:var(--white);letter-spacing:.5px}
.nav-home{left:637px;padding-bottom:6px;border-bottom:2px solid var(--white)}
.nav-services{left:749px}
.nav-booking{left:898px}
.nav-contact{left:1039px}

.booking-bar{left:263px;top:466px;width:684px;height:104px;border-radius:10px;
  background:rgba(255,255,255,.38);box-shadow:0 3px 10px rgba(0,0,0,.18)}
.book-now{left:291px;top:516px;font-size:15px;font-weight:600;color:var(--white)}
.field-label{top:474px;font-size:15px;font-weight:600;color:var(--white);text-align:center}
.field-box{top:499px;height:57px;border-radius:8px;background:var(--teal);color:var(--white);
  font-size:40px;font-weight:400;text-align:center;line-height:57px}
.check-btn{left:778px;top:502px;width:147px;height:54px;border-radius:6px;background:var(--teal-dark);
  color:var(--white);font-size:15px;font-weight:500;text-align:center;line-height:18px;padding-top:9px;
  box-shadow:2px 3px 4px rgba(0,0,0,.3)}

/* services */
.section-title{font-weight:700;color:var(--teal)}
.services-title{left:0;width:1200px;top:638px;text-align:center;font-size:38px}
.service-icon{top:744px;width:104px;height:104px}
.service-text{top:870px;width:220px;font-size:13.6px;line-height:17.2px;text-align:justify;hyphens:auto}

/* newsletter */
.newsletter{left:0;top:1140px;width:1200px;height:281px;background:linear-gradient(90deg,var(--cyan) 0%,var(--cyan) 35%,var(--green) 100%)}
.newsletter-title{left:152px;top:1202px;font-size:24px;font-weight:600;color:var(--white);letter-spacing:-.3px}
.newsletter-input{left:152px;top:1250px;width:414px;height:47px;border-radius:5px;background:var(--white);
  font-size:14px;color:#666;padding:14px 12px}
.newsletter-send{left:618px;top:1250px;width:146px;height:47px;border-radius:4px;background:var(--send-green);
  color:var(--white);font-size:26px;font-weight:600;text-align:center;line-height:47px}

/* about */
.about-brand{left:180px;top:1560px;width:240px;text-align:center;color:var(--brand-blue);font-weight:600}
.about-brand .brand-name{font-size:48px;line-height:56px}
.about-brand .brand-sub{font-size:22px;letter-spacing:10px;line-height:30px}
.about-brand-dot{left:270px;top:1515px;width:60px;height:40px;border-radius:50%;border:3px solid var(--brand-blue)}
.about-divider{left:487px;top:1478px;width:2px;height:295px;background:var(--brand-blue)}
.about-title{left:700px;width:280px;top:1508px;text-align:right;font-size:30px;font-weight:600;color:var(--brand-blue)}
.about-text{left:590px;top:1556px;width:397px;font-size:14.6px;line-height:23.5px;text-align:justify}

/* footer */
.footer{left:0;top:1823px;width:1200px;height:691px;background:var(--cyan)}
.footer-heading{top:1850px;font-size:29px;font-weight:500;color:var(--white)}
.info-line{left:104px;font-size:21px;color:var(--ink)}
.form-label{left:441px;font-size:19px;color:var(--ink)}
.form-field{left:441px;width:280px;background:var(--white);border:1px solid #d7d7d7}
.form-send{left:441px;top:2383px;width:79px;height:34px;background:#000;color:var(--white);
  font-size:19px;text-align:center;line-height:34px;letter-spacing:1px}
.social-square{top:1919px;width:37px;height:37px;border-radius:4px;background:var(--white)}
</style>
</head>
<body>

<div class="abs hero-photo" role="img" aria-label="Photo of a client relaxing face down on a massage table while a therapist works on her shoulders"></div>

<svg class="abs header-band" width="1200" height="240" viewBox="0 0 1200 240" aria-hidden="true">
  <defs>
    <linearGradient id="brandGradient" x1="0" y1="0" x2="1" y2="0">
      <stop offset="0" stop-color="#00cfff"/>
      <stop offset="1" stop-color="#0ce07a"/>
    </linearGradient>
  </defs>
  <path d="M0 0 H1200 V145 C900 150 500 185 270 237 C170 215 80 185 0 160 Z" fill="url(#brandGradient)"/>
</svg>

<div class="abs brand">
  <div class="brand-name">Kelvra's</div>
  <div class="brand-sub">MASSAGE</div>
</div>

<nav>
  <div class="abs nav nav-home">HOME</div>
  <div class="abs nav nav-services">SERVICES</div>
  <div class="abs nav nav-booking">BOOKING</div>
  <div class="abs nav nav-contact">CONTACT</div>
</nav>

<div class="abs booking-bar"></div>
<div class="abs book-now">BOOK NOW!</div>
<div class="abs field-label" style="left:436px;width:80px">DAY</div>
<div class="abs field-label" style="left:528px;width:80px">MONTH</div>
<div class="abs field-label" style="left:625px;width:131px">HOUR</div>
<div class="abs field-box" style="left:436px;width:80px">08</div>
<div class="abs field-box" style="left:528px;width:80px">12</div>
<div class="abs field-box" style="left:625px;width:131px">9:00</div>
<div class="abs check-btn">Check<br>availability</div>

<div class="abs section-title services-title">SERVICES</div>

<svg class="abs service-icon" style="left:246px" viewBox="0 0 104 104" aria-hidden="true">
  <circle cx="52" cy="52" r="49" fill="none" stroke="#14c9b0" stroke-width="3"/>
  <rect x="28" y="38" width="48" height="34" rx="5" fill="#14c9b0"/>
  <path d="M42 38 V31 H62 V38" fill="none" stroke="#14c9b0" stroke-width="4"/>
  <path d="M52 45 V65 M42 55 H62" stroke="#fff" stroke-width="5"/>
</svg>
<svg class="abs service-icon" style="left:558px" viewBox="0 0 104 104" aria-hidden="true">
  <circle cx="52" cy="52" r="49" fill="none" stroke="#14c9b0" stroke-width="3"/>
  <circle cx="52" cy="52" r="28" fill="#14c9b0"/>
  <path d="M30 40 C45 45 50 60 42 77 M74 64 C59 59 54 44 62 27" fill="none" stroke="#fff" stroke-width="3"/>
</svg>
<svg class="abs service-icon" style="left:846px" viewBox="0 0 104 104" aria-hidden="true">
  <circle cx="52" cy="52" r="49" fill="none" stroke="#14c9b0" stroke-width="3"/>
  <rect x="28" y="48" width="11" height="26" fill="#14c9b0"/>
  <path d="M42 48 L52 34 C54 28 60 28 60 34 L58 45 H72 C77 45 78 50 76 53 L72 70 C71 73 69 74 66 74 H42 Z" fill="#14c9b0"/>
</svg>

<p class="abs service-text" style="left:189px">Lorem ipsum dolor sit amet, consectetur adipiscing elit. Nam interdum molestie nisi nec venenatis. In pharetra lacus non erat ornare, sed mollis libero tempus. Nam pellentesque urna dolor. Aenean ut facilisis felis. Etiam at faucibus leo. Fusce ut massa sodales ante semper aliquam eu ut velit.</p>
<p class="abs service-text" style="left:488px">Lorem ipsum dolor sit amet, consectetur adipiscing elit. Nam interdum molestie nisi nec venenatis. In pharetra lacus non erat ornare, sed mollis libero tempus. Nam pellentesque urna dolor. Aenean ut facilisis felis. Etiam at faucibus leo. Fusce ut massa sodales ante semper aliquam eu ut velit.</p>
<p class="abs service-text" style="left:788px">Lorem ipsum dolor sit amet, consectetur adipiscing elit. Nam interdum molestie nisi nec venenatis. In pharetra lacus non erat ornare, sed mollis libero tempus. Nam pellentesque urna dolor. Aenean ut facilisis felis. Etiam at faucibus leo. Fusce ut massa sodales ante semper aliquam eu ut velit.</p>

<section class="abs newsletter"></section>
<div class="abs newsletter-title">SUBSCRIBE TO OUR NEWSLETTER</div>
<div class="abs newsletter-input">e-mail</div>
<div class="abs newsletter-send">SEND</div>

<div class="abs about-brand-dot"></div>
<div class="abs about-brand">
  <div class="brand-name">Kelvra's</div>
  <div class="brand-sub">MASSAGE</div>
</div>
<div class="abs about-divider"></div>
<div class="abs about-title">ABOUT US</div>
<p class="abs about-text">Lorem ipsum dolor sit amet, consectetur adipiscing elit. Nam interdum molestie nisi nec venenatis. In pharetra lacus non erat ornare, sed mollis libero tempus. Nam pellentesque urna dolor. Aenean ut facilisis felis. Etiam at faucibus leo. Fusce ut massa sodales ante semper aliquam eu ut velit.</p>

<footer class="abs footer"></footer>
<div class="abs footer-heading" style="left:104px">INFORMATION</div>
<div class="abs footer-heading" style="left:506px">CONTACT</div>
<div class="abs footer-heading" style="left:843px">SOCIAL LINKS</div>

<div class="abs info-line" style="top:1912px">Str. Lorem ipsum 456</div>
<div class="abs info-line" style="top:1944px">KV2R Fenmore UK</div>
<div class="abs info-line" style="top:2003px">VAT. 047281936</div>
<div class="abs info-line" style="top:2060px">Phone: 739105264</div>

<div class="abs form-label" style="top:1913px">Name</div>
<div class="abs form-field" style="top:1947px;height:37px"></div>
<div class="abs form-label" style="top:1988px">Email</div>
<div class="abs form-field" style="top:2018px;height:38px"></div>
<div class="abs form-label" style="top:2059px">Subject</div>
<div class="abs form-field" style="top:2088px;height:39px"></div>
<div class="abs form-label" style="top:2132px">Message</div>
<div class="abs form-field" style="top:2159px;height:211px"></div>
<div class="abs form-send">SEND</div>

<div class="abs social-square" style="left:846px" aria-label="Social link 1"></div>
<div class="abs social-square" style="left:895px" aria-label="Social link 2"></div>
<div class="abs social-square" style="left:944px" aria-label="Social link 3"></div>

</body>
</html>
```